Branvique needs a business Card Design

We are looking for a business card Design for our new Managed Service Provider Company, Branvique. Branvique encompasses everything IT for the average medium sized business. Our primary services are help desk support, cyber-security (malware and ransomware protection), and Disaster Recovery systems. We would like the design to have a very clean and professional look, with a very minimalist feel.

Target Market(s)

Medium to large sized businesses

Industry/Entity Type

It Service

Contact Information for Business Card

Name GoesHere
name@branvique.com
O: 555-382-6047
C: 555-731-5820

Font styles to use
Other font styles liked:
• Poppins Font Only Please

Colors

Designer to choose only greyscale colors for use in the design.

Requirements
Must have
• Logo included
Nice to have
• Cutting Edge, innovative, minimalistic, elegant

```html
<!DOCTYPE html>
<html lang="en">
<head>
<meta charset="utf-8">
<title>Branvique business card</title>
<link href="https://fonts.googleapis.com/css2?family=Poppins:wght@300;400;600&display=swap" rel="stylesheet">
<style>
  :root {
    --stage: #8c8c8c;
    --navy: #0b2440;
    --white: #ffffff;
    --ink: #0b2440;
    --muted: #6f7680;
    --stripe: #a9abae;
  }
  * { box-sizing: border-box; margin: 0; padding: 0; }
  html, body {
    width: 1200px; height: 675px; overflow: hidden;
    background: var(--stage);
    font-family: "Poppins", sans-serif;
  }
  .stage {
    width: 1200px; height: 675px;
    display: flex; align-items: center; justify-content: center; gap: 40px;
  }
  .card {
    position: relative;
    width: 520px; height: 297px;
    box-shadow: 0 6px 18px rgba(0,0,0,0.25);
    overflow: hidden;
  }
  .card--back { background: var(--navy); }
  .card--back .wordmark {
    position: absolute; right: 34px; bottom: 52px;
    color: var(--white);
    font-weight: 300; font-size: 26px; letter-spacing: 10px;
  }
  .card--front { background: var(--white); }
  .swoosh { position: absolute; inset: 0; }
  .brand {
    position: absolute; left: 52px; top: 150px;
    color: var(--ink);
    font-weight: 300; font-size: 23px; letter-spacing: 8px;
  }
  .divider {
    position: absolute; left: 262px; top: 72px;
    width: 1px; height: 92px; background: var(--ink); opacity: 0.7;
  }
  .contact {
    position: absolute; left: 282px; top: 70px;
    color: var(--ink);
  }
  .contact__name { font-weight: 600; font-size: 15px; line-height: 1.1; }
  .contact__role { font-weight: 400; font-size: 10px; color: var(--muted); margin-bottom: 10px; }
  .contact__line {
    display: flex; align-items: center; gap: 6px;
    font-weight: 400; font-size: 11px; line-height: 17px; color: #2e3640;
  }
  .contact__line svg { width: 10px; height: 10px; fill: var(--ink); flex: none; }
</style>
</head>
<body>
<main class="stage">
  <section class="card card--back" aria-label="Card back">
    <div class="wordmark">BRANVIQUE</div>
  </section>

  <section class="card card--front" aria-label="Card front">
    <svg class="swoosh" viewBox="0 0 520 297" preserveAspectRatio="none" aria-hidden="true">
      <path d="M0 280 Q300 250 520 142 L520 152 Q300 262 0 290 Z" fill="var(--stripe)"/>
      <path d="M0 290 Q300 262 520 152 L520 297 L0 297 Z" fill="var(--navy)"/>
    </svg>
    <div class="brand">BRANVIQUE</div>
    <div class="divider"></div>
    <div class="contact">
      <div class="contact__name">MARA KELLWORTH</div>
      <div class="contact__role">Owner</div>
      <div class="contact__line">
        <svg viewBox="0 0 24 24"><path d="M6.6 10.8a15 15 0 0 0 6.6 6.6l2.2-2.2c.3-.3.7-.4 1-.2 1.1.4 2.3.6 3.6.6.6 0 1 .4 1 1V20c0 .6-.4 1-1 1A17 17 0 0 1 3 4c0-.6.4-1 1-1h3.5c.6 0 1 .4 1 1 0 1.3.2 2.5.6 3.6.1.3 0 .7-.2 1z"/></svg>
        555-382-6047
      </div>
      <div class="contact__line">
        <svg viewBox="0 0 24 24"><path d="M7 1h10a2 2 0 0 1 2 2v18a2 2 0 0 1-2 2H7a2 2 0 0 1-2-2V3a2 2 0 0 1 2-2zm0 3v15h10V4z"/></svg>
        555-731-5820
      </div>
      <div class="contact__line">
        <svg viewBox="0 0 24 24"><path d="M2 5h20v14H2zm2 2v.5l8 5 8-5V7z"/></svg>
        name@branvique.com
      </div>
    </div>
  </section>
</main>
</body>
</html>
```